Brochure Design - Non-Profit Fundraising Stream

We are a non-profit organization that is developing a fundraising project through the donation of life insurance policies. We have three brochures in each English and French that we developed for a sister organization that we want to reintegrate with our Foundation, keeping the same copy text just changing the logos, colors and make it overall more visually appealing. The foundation is called the 'Varnek-Holt Syndrome Foundation Canada'.
The original files in .docx format are attached as is the full logo and two symbol files. The deliverables would be six documents in total (InDesign or .docx), each brochure in English and French. The color hex codes are:
red: #7b2850
dark blue: #2c79a7
pale blue: #78b2e2

```html
<!DOCTYPE html>
<html lang="en">
<head>
<meta charset="utf-8">
<title>Varnek-Holt Syndrome Foundation Canada – Donation Process</title>
<link rel="stylesheet" href="https://fonts.googleapis.com/css2?family=Lato:wght@400;700;900&family=Oswald:wght@500;600&display=swap">
<style>
  :root {
    --red: #7b2850;
    --dark-blue: #2c79a7;
    --pale-blue: #78b2e2;
    --backdrop: #e4e4e4;
    --paper: #ffffff;
    --ink: #3b3b3b;
  }
  * { box-sizing: border-box; margin: 0; padding: 0; }
  html, body { width: 1200px; height: 900px; overflow: hidden; }
  body {
    background: var(--backdrop);
    font-family: "Lato", Arial, sans-serif;
    color: var(--ink);
    position: relative;
  }
  .flyer {
    position: absolute;
    left: 280px; top: 10px;
    width: 640px; height: 880px;
    background: var(--paper);
    box-shadow: 0 6px 24px rgba(0,0,0,.12);
  }
  .flyer > * { position: absolute; }

  .brand { left: 140px; top: 44px; width: 380px; display: flex; align-items: center; justify-content: center; gap: 10px; }
  .brand-dot { width: 22px; height: 22px; border-radius: 50%; background: var(--pale-blue); flex: none; }
  .brand-name { font-size: 17px; font-weight: 400; color: var(--dark-blue); line-height: 1.2; }

  .intro { left: 150px; top: 104px; width: 370px; font-size: 10px; line-height: 1.55; color: var(--ink); }
  .intro p + p { margin-top: 8px; }
  .intro strong { font-weight: 700; }
  .intro .accent { color: var(--red); }

  .band {
    left: 130px; right: 30px; height: 52px; border-radius: 26px;
    background: var(--dark-blue); color: #fff;
    font-size: 10px; line-height: 1.45; padding: 10px 30px 10px 34px;
    display: flex; align-items: center;
  }
  .band--intro { top: 220px; background: var(--pale-blue); }
  .band--final { top: 760px; font-size: 11px; font-weight: 700; }

  .section-title {
    left: 130px; width: 230px; top: 286px; text-align: center;
    font-family: "Oswald", "Arial Narrow", sans-serif; font-weight: 600;
    font-size: 17px; letter-spacing: 1px; color: var(--red);
  }
  .submit { left: 130px; top: 316px; width: 225px; font-size: 10px; }
  .submit-lead { font-weight: 700; color: var(--dark-blue); line-height: 1.4; margin-bottom: 6px; }
  .submit-lead span { color: var(--red); }
  .submit-list { list-style: none; columns: 2; column-gap: 10px; font-size: 9px; line-height: 1.6; color: var(--ink); }
  .submit-list li::before { content: "•"; color: var(--red); margin-right: 5px; }

  .marker {
    width: 66px; height: 66px; border-radius: 50%;
    border: 3px solid var(--dark-blue); background: #fff;
    display: flex; align-items: center; justify-content: center;
    font-family: "Oswald", "Arial Narrow", sans-serif; font-weight: 600;
    font-size: 17px; color: var(--dark-blue); letter-spacing: .5px;
  }
  .marker--start { left: 40px; top: 404px; }
  .marker--end { left: 40px; top: 753px; }
  .connector { background: var(--dark-blue); }
  .connector--start { left: 106px; top: 436px; width: 249px; height: 3px; }
  .connector--drop { left: 71px; top: 470px; width: 3px; height: 24px; }
  .connector--end { left: 106px; top: 785px; width: 26px; height: 3px; }

  .steps { list-style: none; width: 230px; }
  .steps--left { left: 50px; top: 494px; }
  .steps--right { left: 372px; top: 312px; }
  .step { display: flex; align-items: center; height: 44px; margin-bottom: 8px; }
  .step-num {
    width: 40px; height: 40px; border-radius: 50%; flex: none;
    border: 3px solid var(--red); background: #fff; color: var(--red);
    font-family: "Oswald", "Arial Narrow", sans-serif; font-weight: 500; font-size: 15px;
    display: flex; align-items: center; justify-content: center;
    position: relative; z-index: 1;
  }
  .step-text {
    flex: 1; height: 44px; margin-left: -8px; padding: 0 12px 0 18px;
    background: var(--red); color: #fff; border-radius: 0 10px 10px 0;
    font-size: 9px; line-height: 1.35; display: flex; align-items: center;
  }

  .call { right: 40px; top: 600px; text-align: right; }
  .call-line { font-family: "Oswald", "Arial Narrow", sans-serif; font-weight: 600; font-size: 15px; color: var(--ink); letter-spacing: .5px; }
  .call-mail { font-size: 9px; color: var(--red); margin-top: 2px; }

  .dot-field {
    left: 130px; top: 814px; width: 230px; height: 60px; border-radius: 30px 30px 0 0;
    background: radial-gradient(ellipse at center, rgba(120,178,226,.45), rgba(120,178,226,0) 70%);
  }
</style>
</head>
<body>
<main class="flyer">
  <header class="brand">
    <span class="brand-dot"></span>
    <span class="brand-name">Varnek-Holt Syndrome Foundation Canada</span>
  </header>

  <section class="intro">
    <p><strong>Varnek-Holt Syndrome Foundation of Canada (VHSFC)</strong> has partnered with Mirelle Charity Services (MCS) to launch <strong class="accent">VHSF Canada</strong> Planned Giving Plus program to finance medical research and support.</p>
    <p>Mirelle Charity Services (MCS) has developed the following streamlined process to evaluate potential life insurance donations.</p>
  </section>

  <div class="band band--intro">Donors may give a new or existing life insurance policy, naming VHSFC as owner and beneficiary of the full amount.</div>

  <h2 class="section-title">DONATION PROCESS</h2>

  <section class="submit">
    <p class="submit-lead">Submit case with the following info to <span>donations@mirellegiving.com</span></p>
    <ul class="submit-list">
      <li>Client name</li>
      <li>Policy number</li>
      <li>Carrier</li>
      <li>Face amount</li>
      <li>Policy type</li>
      <li>Age, health</li>
      <li>Premiums</li>
      <li>Beneficiary</li>
      <li>Cash value</li>
      <li>Illustration</li>
    </ul>
  </section>

  <div class="marker marker--start">START</div>
  <div class="connector connector--start"></div>
  <div class="connector connector--drop"></div>

  <ol class="steps steps--left">
    <li class="step"><span class="step-num">02</span><span class="step-text">MCS will review case and advise client in writing</span></li>
    <li class="step"><span class="step-num">03</span><span class="step-text">If accepted, donor signs ownership change forms with carrier</span></li>
    <li class="step"><span class="step-num">04</span><span class="step-text">Medical and underwriting records sent to MCS for review</span></li>
    <li class="step"><span class="step-num">05</span><span class="step-text">MCS confirms the policy value and terms with VHSFC</span></li>
    <li class="step"><span class="step-num">06</span><span class="step-text">VHSFC will provide an estimated value of donation</span></li>
  </ol>

  <ol class="steps steps--right">
    <li class="step"><span class="step-num">07</span><span class="step-text">Client signs irrevocable transfer of policy to VHSFC</span></li>
    <li class="step"><span class="step-num">08</span><span class="step-text">VHSFC submits change of owner forms to the insurance carrier</span></li>
    <li class="step"><span class="step-num">09</span><span class="step-text">Carrier processes request and issues confirmation letter</span></li>
    <li class="step"><span class="step-num">10</span><span class="step-text">Insurance carrier confirms transfer of ownership to VHSFC</span></li>
    <li class="step"><span class="step-num">11</span><span class="step-text">VHSFC issues tax receipt and thank-you letter to donor</span></li>
  </ol>

  <div class="call">
    <p class="call-line">CALL US: 1 (800) 555-0142</p>
    <p class="call-mail">donations@mirellegiving.com</p>
  </div>

  <div class="band band--final">Once transfer is confirmed by Carrier, VHSFC converts policy to permanent (if term)</div>

  <div class="dot-field" role="img" aria-label="Decorative field of soft blue dots with a small heart"></div>
  <div class="marker marker--end">END</div>
  <div class="connector connector--end"></div>
</main>
</body>
</html>
```